Package Design - Disposable Face Towel

Hi,

We are needing assistance with graphic design on our box/carton/package.

The attached image that is white is our biggest competitor.

Our brand is "BRIGHT DEW LABS" Please see the logo we uploaded.

Oder we have in mind for front of box:

Logo
LARGE TOWELS
50 Count
Ultra Soft| 100% USDA Bio-Based|100% Eucalyptus Viscose | Vegan
BRIGHTDEWLABS.EXAMPLE

We like medium to dark blue on most of the box, with white and minimal hot pink or salmon. Something that is sharp, modern, and stands out from our competitors.

Box dimensions are: 6.25 x 5.25 x 4.75 inches

This will be 1 of many design projects.

Target Market(s)

Female Beauty Products

Font styles to use
Serif
Sans Serif

Colors
0054AA
0677BA
7BADD7
CADEEF
E8F1F8
EB3D1F
EC4F4E
F09395
F8D3D4
FCEDEE

Requirements
Must have
• Needs to look sharp and modern

```html
<!DOCTYPE html>
<html lang="en">
<head>
<meta charset="utf-8">
<title>Bright Dew Labs – Large Towels XL Carton Dieline</title>
<link rel="stylesheet" href="https://fonts.googleapis.com/css2?family=Cinzel:wght@400&family=Montserrat:wght@400;500;700&display=swap">
<style>
  :root {
    --bg: #ffffff;
    --blue-deep: #0054AA;
    --blue-mid: #0677BA;
    --blue-back: #004c9c;
    --blue-soft: #7BADD7;
    --blue-pale: #CADEEF;
    --blue-mist: #E8F1F8;
    --pink-hot: #EC4F4E;
    --pink-salmon: #F09395;
    --white: #ffffff;
    --grey-ink: #5e6f82;
  }
  html, body {
    margin: 0;
    padding: 0;
    background: var(--bg);
    overflow: hidden;
  }
  .dieline {
    display: block;
    width: 982px;
    height: 1200px;
  }
  .panel { fill: var(--blue-deep); }
  .panel--tab { fill: var(--blue-mid); }
  .panel--back { fill: var(--blue-back); }
  .fold-line { stroke: var(--blue-soft); stroke-width: 0.7; fill: none; }
  .perforation { stroke: var(--blue-pale); stroke-width: 0.7; fill: none; stroke-dasharray: 3 2; }
  .dispenser-cut { stroke: var(--blue-pale); stroke-width: 0.8; fill: none; }
  .label-panel { fill: var(--blue-mist); }
  .feature-band { fill: var(--pink-hot); }
  .brand-name {
    font-family: "Cinzel", serif;
    font-weight: 400;
    fill: var(--white);
  }
  .brand-mark { fill: var(--white); }
  .product-title {
    font-family: "Montserrat", sans-serif;
    font-weight: 700;
    font-size: 12.5px;
    fill: var(--blue-deep);
  }
  .tagline, .feature-text, .size-note, .web-address {
    font-family: "Montserrat", sans-serif;
    font-weight: 400;
  }
  .tagline { font-size: 7.3px; fill: var(--blue-deep); }
  .feature-text { font-size: 7.2px; fill: var(--white); }
  .count {
    font-family: "Montserrat", sans-serif;
    font-weight: 700;
    font-size: 8.8px;
    fill: var(--blue-deep);
  }
  .size-note { font-size: 5.8px; fill: var(--grey-ink); }
  .web-address { font-size: 7.6px; fill: var(--grey-ink); letter-spacing: 0.3px; }
</style>
</head>
<body>
<svg class="dieline" viewBox="0 0 982 1200" xmlns="http://www.w3.org/2000/svg">
  <!-- side glue tabs -->
  <path class="panel--tab" d="M42 302 H24 Q1 302 1 325 V578 Q1 601 24 601 H42 Z"/>
  <path class="panel--tab" d="M940 302 H958 Q981 302 981 325 V578 Q981 601 958 601 H940 Z"/>

  <!-- top lid panel -->
  <rect class="panel" x="313" y="0" width="356" height="301"/>

  <!-- main band: side, front top, side -->
  <rect class="panel" x="42" y="300" width="898" height="300"/>

  <!-- dispenser flap panel -->
  <path class="panel" d="M312 600 H670 Q710 600 710 640 V859 Q710 899 670 899 H312 Q272 899 272 859 V640 Q272 600 312 600 Z"/>

  <!-- back panel -->
  <rect class="panel--back" x="313" y="899" width="356" height="301"/>

  <!-- fold lines -->
  <line class="fold-line" x1="313" y1="300" x2="669" y2="300"/>
  <line class="fold-line" x1="42" y1="300" x2="42" y2="600"/>
  <line class="fold-line" x1="940" y1="300" x2="940" y2="600"/>
  <line class="fold-line" x1="313" y1="300" x2="313" y2="1200"/>
  <line class="fold-line" x1="669" y1="300" x2="669" y2="1200"/>
  <line class="fold-line" x1="42" y1="600" x2="940" y2="600"/>

  <!-- perforated opening guide -->
  <rect class="perforation" x="367" y="450" width="248" height="280"/>

  <!-- dispenser slot cut -->
  <path class="dispenser-cut" d="M357 724 L369 733 L372 729 H398 L401 727 H412 L415 729 H434 L437 727 H455 L458 729 H476 L479 727 H498 L501 729 H519 L522 727 H541 L544 729 H562 L565 727 H580 L583 729 H609 L612 733 L625 724 Q640 730 640 749 Q640 768 625 775 L612 769 L609 772 H583 L580 770 H565 L562 772 H544 L541 770 H522 L519 772 H501 L498 770 H479 L476 772 H458 L455 770 H437 L434 772 H415 L412 770 H401 L398 772 H372 L369 769 L357 775 Q342 768 342 749 Q342 730 357 724 Z"/>

  <!-- front brand lockup -->
  <text class="brand-name" x="406" y="530" font-size="16" textLength="142" lengthAdjust="spacingAndGlyphs">BRIGHT DEW LABS</text>
  <rect class="brand-mark" x="555" y="514" width="16" height="16"/>

  <!-- flap brand lockup -->
  <text class="brand-name" x="428" y="674" font-size="11.5" textLength="102" lengthAdjust="spacingAndGlyphs">BRIGHT DEW LABS</text>
  <rect class="brand-mark" x="536" y="662" width="12" height="12"/>

  <!-- product label triangle -->
  <polygon class="label-panel" points="491,721 669,899 313,899"/>

  <text class="product-title" x="491" y="815" text-anchor="middle">LARGE TOWELS XL</text>
  <text class="tagline" x="491" y="827" text-anchor="middle">Nature's best gift to your skin</text>
  <text class="tagline" x="491" y="836" text-anchor="middle">wrapped in a soft, absorbent towel</text>

  <polygon class="feature-band" points="366,846 545,846 549,856 545,867 345,867"/>
  <text class="feature-text" x="533" y="854" text-anchor="end">Ultra Soft | 100% USDA  Bio-based</text>
  <text class="feature-text" x="533" y="863" text-anchor="end">100%  Eucalyptus  Viscose  |  Vegan</text>

  <text class="count" x="552" y="857">50 COUNT</text>
  <text class="size-note" x="552" y="866">Size: 10inch x 12inch</text>

  <text class="web-address" x="491" y="884" text-anchor="middle">BRIGHTDEWLABS.EXAMPLE</text>
</svg>
</body>
</html>
```